QorLa Drift Bhutan Trip

This is a one-page (A5) flyer to attract sign ups for Bhutan Trip.

Target Market(s)

Young entrepreneurs (worldwide)

Requirements
Must have
• Must have "WOW" effect and attract sign ups
Nice to have
• Striking and vibrant

```html
<!DOCTYPE html>
<html lang="en">
<head>
<meta charset="utf-8">
<title>QorLa Drift Bhutan Trip – Flyer</title>
<link href="https://fonts.googleapis.com/css2?family=Luckiest+Guy&family=Roboto+Condensed:ital,wght@0,400;0,700;1,400;1,700;1,900&family=Open+Sans:wght@400;600&display=swap" rel="stylesheet">
<style>
  :root{
    --stage:#56801f;
    --leaf:#6cb33f;
    --leaf-dark:#4f8f22;
    --crimson:#c4202a;
    --crimson-dark:#9c1820;
    --sun:#f3dc10;
    --magenta:#d6248f;
    --sky:#29a9e0;
    --ink:#111;
    --grey:#5a5a5a;
    --paper:#ffffff;
  }
  *{margin:0;padding:0;box-sizing:border-box}
  html,body{width:1200px;height:1200px;overflow:hidden;background:var(--stage)}
  .flyer{position:absolute;left:210px;top:50px;width:780px;height:1100px;background:var(--paper);overflow:hidden;font-family:"Open Sans",sans-serif;border-bottom:10px solid var(--leaf)}
  .hero-photo{position:absolute;left:0;top:0;width:780px;height:620px;
    background:linear-gradient(90deg,#5b6b4a 0%,#7d8a6a 25%,#6a8a45 45%,var(--leaf) 70%,var(--leaf) 100%)}
  .shapes{position:absolute;left:0;top:0}
  .brand-tag{position:absolute;left:26px;top:20px;width:130px;height:70px;background:var(--paper);display:flex;align-items:center;justify-content:center;font:700 22px "Roboto Condensed",sans-serif;color:var(--magenta)}
  .title{position:absolute;left:380px;top:120px;width:380px;text-align:right;font-family:"Luckiest Guy",cursive;font-size:44px;line-height:1.05;color:var(--magenta);-webkit-text-stroke:1px #fff}
  .tagline{position:absolute;left:420px;top:240px;width:340px;text-align:right;font:italic 400 26px/1.15 "Roboto Condensed",sans-serif;color:#fff}
  .tagline b{color:var(--ink);font-weight:700}
  .collage{position:absolute;left:440px;top:440px;width:320px;height:270px}
  .collage .tile{position:absolute;width:152px;height:128px;border:4px solid var(--sky)}
  .t1{left:0;top:0;background:linear-gradient(160deg,#7da0b8,#8a6a4a)}
  .t2{left:162px;top:0;background:linear-gradient(160deg,#bcd3e6,#a0443a)}
  .t3{left:0;top:138px;background:linear-gradient(160deg,#9cc0e0,#e8e6e0 60%,#6a6a4a)}
  .t4{left:162px;top:138px;background:linear-gradient(160deg,#b23a4a,#d9a880 60%,#6a4a3a)}
  .date-badge{position:absolute;left:110px;top:85px;width:100px;height:100px;border-radius:50%;background:var(--sun);border:3px dashed #fff;display:flex;flex-direction:column;align-items:center;justify-content:center;font-family:"Roboto Condensed",sans-serif}
  .date-badge .days{font:italic 900 40px/1 "Roboto Condensed",sans-serif;color:var(--ink)}
  .date-badge .month{margin-top:2px;background:var(--ink);color:#fff;font:italic 700 11px "Roboto Condensed",sans-serif;padding:1px 6px}
  .highlights-label{position:absolute;left:40px;top:590px;background:var(--sun);padding:4px 22px;font:italic 700 36px "Roboto Condensed",sans-serif;color:var(--ink)}
  .item{position:absolute;width:230px}
  .item h3{font:italic 700 27px/1 "Roboto Condensed",sans-serif;color:var(--leaf)}
  .item p{font-size:15px;line-height:1.3;color:var(--grey);margin-top:4px}
  .price-box{position:absolute;left:240px;top:880px;width:300px;background:var(--sun);padding:10px 16px;border-radius:6px;color:var(--ink)}
  .price-box .price{font:italic 900 36px/1 "Roboto Condensed",sans-serif}
  .price-box .early{font:italic 700 18px "Roboto Condensed",sans-serif;margin-top:4px}
  .price-box .note{font:italic 700 12px "Roboto Condensed",sans-serif}
  .partners{position:absolute;left:20px;top:975px;width:420px;height:110px;display:flex;align-items:center;gap:14px}
  .partner-group{display:flex;flex-direction:column;justify-content:center;height:100%;padding-right:14px;border-right:1px solid #ccc}
  .partner-group:last-child{border-right:none}
  .caption{font-size:10px;color:var(--grey);margin-bottom:6px}
  .partner-name{font:700 18px "Roboto Condensed",sans-serif;color:var(--magenta);display:flex;align-items:center;gap:6px}
  .partner-name.teal{color:#1f6f80}
  .partner-name.green{color:var(--leaf-dark)}
  .partner-name .dot{width:14px;height:14px;border-radius:50%;background:currentColor}
  .partner-row{display:flex;gap:14px}
  .register{position:absolute;left:460px;top:985px;width:300px;border-left:1px solid #ccc;padding-left:18px}
  .register h2{font:italic 700 32px/1 "Roboto Condensed",sans-serif;color:var(--leaf)}
  .register .limit{font:italic 700 17px "Roboto Condensed",sans-serif;color:#333;margin-top:6px}
  .register .limit span,.register .mail span{color:var(--leaf)}
  .register .mail{font:italic 700 16px "Roboto Condensed",sans-serif;color:#333;margin-top:2px}
</style>
</head>
<body>
<main class="flyer">
  <div class="hero-photo" role="img" aria-label="Suspension bridge draped with prayer flags leading to a Bhutanese temple on a green hillside"></div>

  <svg class="shapes" width="780" height="1100" viewBox="0 0 780 1100" aria-hidden="true">
    <polygon points="0,520 780,440 780,760 0,560" fill="var(--crimson)"/>
    <polygon points="0,560 780,760 780,440 600,470" fill="var(--crimson-dark)" opacity=".35"/>
    <polygon points="0,560 780,760 780,1100 0,1100" fill="var(--paper)"/>
    <polygon points="0,560 420,668 0,760" fill="#f2f2f2" opacity=".7"/>
  </svg>

  <div class="brand-tag">QorLa Drift</div>

  <h1 class="title">QorLa Drift<br>Bhutan Trip</h1>
  <p class="tagline"><b>Sign up</b> for a once in a lifetime experience in the land of happiness!</p>

  <div class="collage">
    <div class="tile t1" role="img" aria-label="Riverside dzong fortress among mountains"></div>
    <div class="tile t2" role="img" aria-label="Ornate temple courtyard with red painted facade"></div>
    <div class="tile t3" role="img" aria-label="White dzong towers under a blue sky"></div>
    <div class="tile t4" role="img" aria-label="Crowd gathered at a colourful festival"></div>
    <div class="date-badge"><span class="days">3-6</span><span class="month">July 2017</span></div>
  </div>

  <div class="highlights-label">Highlights</div>

  <div class="item" style="left:40px;top:655px"><h3>1- LEARN</h3><p>from Leading Social Change Makers.</p></div>
  <div class="item" style="left:40px;top:740px"><h3>4- SAVOUR</h3><p>Organic food.</p></div>
  <div class="item" style="left:40px;top:810px"><h3>7- REJUVENATE</h3><p>your mind, body and soul.</p></div>

  <div class="item" style="left:300px;top:700px"><h3>2- ENGAGE</h3><p>the community through volunteering.</p></div>
  <div class="item" style="left:300px;top:790px"><h3>5- IMMERSE</h3><p>in traditional sports and craft.</p></div>

  <div class="item" style="left:560px;top:790px"><h3>3- DISCOVER</h3><p>your inner happiness.</p></div>
  <div class="item" style="left:560px;top:880px"><h3>6- EXPERIENCE</h3><p>warm Bhutanese hospitality.</p></div>

  <div class="price-box">
    <div class="price">Price at USD2800</div>
    <div class="early">Early bird discount USD2300</div>
    <div class="note">(if you sign up by 31 March 2017)</div>
  </div>

  <div class="partners">
    <div class="partner-group">
      <div class="caption">Exclusively Brought<br>To You By:</div>
      <div class="partner-name">QorLa Drift</div>
    </div>
    <div class="partner-group">
      <div class="caption">&nbsp;</div>
      <div class="partner-name teal"><span class="dot"></span>Arbora</div>
    </div>
    <div class="partner-group">
      <div class="caption">Supported By:</div>
      <div class="partner-row">
        <div class="partner-name teal">Trekvale</div>
        <div class="partner-name green"><span class="dot"></span>Lumen Trust</div>
      </div>
    </div>
  </div>

  <div class="register">
    <h2>Register now!</h2>
    <p class="limit">Limited to <span>30 participants!</span></p>
    <p class="mail"><span>Email:</span> hello@lumentrust.org</p>
  </div>
</main>
</body>
</html>
```